Power Washing Business Easy Postcard Design

We need a postcard designed for our company, which does residential power washing. We clean houses, decks, driveways and fences. The design should be understated, high end with minimalist graphics. No bubbles or wild colors. The name of the business is "stoneridge power washing" which should be rendered all lower case in a san serif font. Sample files in blue or white are attached. The attached files aren't our logo, just a model. The font doesn't have to be exact and "power washing" needs to be added to it.The postcard size is the Marlo Press 8.64" X 5.59". The photo which is attached should fill the whole front of the card.

The text elements on the front are:
1) "stoneridge power washing"- as per the attached files, can be broken into two lines

2) "Mention this card and receive a FREE standard size Deck Wash"

3) "804-555-3186"

4) "stoneridgepowerwashing.example" (this font size can be smaller than the phone number.)

5)"We Clean:- Houses- Decks- Driveways- Fences"The arrangement is the text is up to you. The text should not overpower the image.

Target Market(s)

Homeowners

Industry/Entity Type

Residential

Font styles to use
Sans Serif

Requirements
Should not have
• Garish graphics

```html
<!DOCTYPE html>
<html lang="en">
<head>
<meta charset="utf-8">
<title>stoneridge power washing — postcard</title>
<link href="https://fonts.googleapis.com/css2?family=Questrial&display=swap" rel="stylesheet">
<style>
  :root {
    --navy: #1f2a63;
    --navy-band: #24306e;
    --white: #ffffff;
    --stage: #e9e7e3;
    --header-top: #b9c6e6;
    --header-bottom: #dfe5f4;
    --rule: #d4d4d4;
    --stamp: #e4e4e4;
    --sky: #a9b6dc;
    --dusk: #cfc6d6;
    --glow: #f3d9a6;
    --facade: #8c8a8f;
    --paving: #8b6f58;
    --lawn: #3f5a2a;
  }
  * { margin: 0; padding: 0; box-sizing: border-box; }
  html, body {
    width: 1200px; height: 1000px; overflow: hidden;
    background: var(--stage);
    font-family: "Questrial", "Century Gothic", sans-serif;
    color: var(--navy);
  }
  .canvas { position: relative; width: 1200px; height: 1000px; }

  /* Front of card */
  .card-front {
    position: absolute; left: 53px; top: 52px; width: 687px; height: 436px;
    overflow: hidden; background: var(--white);
  }
  .front-header {
    position: absolute; left: 0; top: 0; width: 100%; height: 92px;
    background: linear-gradient(180deg, var(--header-top), var(--header-bottom));
  }
  .front-wordmark { position: absolute; left: 26px; top: 22px; line-height: 1; -webkit-text-stroke: 0.3px var(--navy); }
  .front-wordmark .name-main { display: block; font-size: 36px; letter-spacing: -0.5px; }
  .front-wordmark .name-sub { display: block; font-size: 25px; margin-top: 1px; }
  .front-contact { position: absolute; right: 20px; top: 25px; text-align: right; line-height: 1; -webkit-text-stroke: 0.3px var(--navy); }
  .front-contact .phone { display: block; font-size: 31px; }
  .front-contact .web { display: block; font-size: 15px; margin-top: 7px; -webkit-text-stroke: 0; }

  .front-photo {
    position: absolute; left: 0; top: 92px; width: 100%; height: 344px;
    background:
      radial-gradient(ellipse 34% 22% at 38% 62%, rgba(250,226,170,0.85), rgba(250,226,170,0) 100%),
      radial-gradient(ellipse 22% 16% at 62% 48%, rgba(247,232,196,0.75), rgba(247,232,196,0) 100%),
      radial-gradient(ellipse 18% 14% at 76% 70%, rgba(236,230,214,0.8), rgba(236,230,214,0) 100%),
      radial-gradient(ellipse 55% 38% at 52% 50%, rgba(124,124,134,0.55), rgba(124,124,134,0) 100%),
      radial-gradient(ellipse 26% 20% at 96% 62%, rgba(55,72,44,0.8), rgba(55,72,44,0) 100%),
      radial-gradient(ellipse 45% 18% at 15% 92%, rgba(63,90,42,0.9), rgba(63,90,42,0) 100%),
      linear-gradient(180deg, var(--sky) 0%, var(--dusk) 30%, #a79c98 52%, var(--facade) 66%, var(--paving) 80%, #5e5a3e 90%, var(--lawn) 100%);
  }
  .offer-band {
    position: absolute; left: 0; top: 364px; width: 100%; height: 34px;
    background: var(--navy-band); color: var(--white);
    font-size: 20.5px; text-align: center; line-height: 34px;
    -webkit-text-stroke: 0.3px var(--white);
  }
  .service-list {
    position: absolute; left: 0; top: 407px; width: 100%;
    display: flex; justify-content: center; align-items: center; gap: 24px;
    color: var(--white); font-size: 15px; list-style: none;
  }
  .service-list .label { margin-right: -8px; }
  .service-list li { display: flex; align-items: center; gap: 8px; }
  .service-list svg { width: 11px; height: 11px; }

  /* Back of card */
  .card-back {
    position: absolute; left: 470px; top: 517px; width: 692px; height: 448px;
    background: var(--white);
  }
  .back-wordmark {
    position: absolute; left: 0; top: 37px; width: 353px; height: 84px;
    background: var(--navy); color: var(--white); text-align: center; line-height: 1;
    padding-top: 6px; -webkit-text-stroke: 0.3px var(--white);
  }
  .back-wordmark .name-main { display: block; font-size: 45px; letter-spacing: -0.5px; }
  .back-wordmark .name-sub { display: block; font-size: 31px; }
  .back-contact { position: absolute; left: 67px; top: 135px; line-height: 1; }
  .back-contact .phone { display: block; font-size: 36px; -webkit-text-stroke: 0.3px var(--navy); }
  .back-contact .web { display: block; font-size: 16px; margin-top: 6px; }
  .stamp-box {
    position: absolute; left: 586px; top: 18px; width: 80px; height: 91px;
    border: 2px solid var(--stamp);
  }
  .address-lines { position: absolute; left: 477px; top: 238px; width: 189px; }
  .address-lines span { display: block; height: 27px; border-bottom: 1px solid var(--rule); }
  .address-lines span:first-child { height: 0; }
</style>
</head>
<body>
<main class="canvas">
  <section class="card-front" aria-label="Postcard front">
    <div class="front-photo" role="img" aria-label="Photo of a large two-storey shingled house with warmly lit windows and porch at dusk, two garage doors, paved driveway and green lawn"></div>
    <header class="front-header">
      <div class="front-wordmark">
        <span class="name-main">stoneridge</span>
        <span class="name-sub">power washing</span>
      </div>
      <div class="front-contact">
        <span class="phone">804-555-3186</span>
        <span class="web">stoneridgepowerwashing.example</span>
      </div>
    </header>
    <p class="offer-band">Mention this card and receive a FREE standard size Deck Wash</p>
    <ul class="service-list">
      <li class="label">We Clean:</li>
      <li><svg viewBox="0 0 11 11"><rect width="11" height="11" fill="#fff"/><path d="M2.3 5.6l2.2 2.2 4.2-4.6" stroke="#1f2a63" stroke-width="1.8" fill="none"/></svg>Houses</li>
      <li><svg viewBox="0 0 11 11"><rect width="11" height="11" fill="#fff"/><path d="M2.3 5.6l2.2 2.2 4.2-4.6" stroke="#1f2a63" stroke-width="1.8" fill="none"/></svg>Decks</li>
      <li><svg viewBox="0 0 11 11"><rect width="11" height="11" fill="#fff"/><path d="M2.3 5.6l2.2 2.2 4.2-4.6" stroke="#1f2a63" stroke-width="1.8" fill="none"/></svg>Driveways</li>
      <li><svg viewBox="0 0 11 11"><rect width="11" height="11" fill="#fff"/><path d="M2.3 5.6l2.2 2.2 4.2-4.6" stroke="#1f2a63" stroke-width="1.8" fill="none"/></svg>Fences</li>
    </ul>
  </section>

  <section class="card-back" aria-label="Postcard back">
    <div class="back-wordmark">
      <span class="name-main">stoneridge</span>
      <span class="name-sub">power washing</span>
    </div>
    <div class="back-contact">
      <span class="phone">804-555-3186</span>
      <span class="web">stoneridgepowerwashing.example</span>
    </div>
    <div class="stamp-box"></div>
    <div class="address-lines"><span></span><span></span><span></span><span></span><span></span></div>
  </section>
</main>
</body>
</html>
```